Namibia currently imports 60% of its food. Meridale Field Trust is an initiative which will assist Namibia to become self sustainable in terms of food production. We aim to do this through the development of 3 agricultural production zones which will include farming zones, local farmer assistance, processing and distribution of the final products. Please see our project overview attached.

```html
<!DOCTYPE html>
<html lang="en">
<head>
<meta charset="utf-8">
<title>Meridale Field Trust</title>
<link href="https://fonts.googleapis.com/css2?family=Merriweather:wght@300;400;700&display=swap" rel="stylesheet">
<style>
:root{
  --green:#10683a;
  --green-dark:#0b5a30;
  --tan:#c8a27c;
  --tan-band:#b99a73;
  --text:#3a3a3a;
  --white:#ffffff;
}
*{margin:0;padding:0;box-sizing:border-box}
html,body{width:1200px;height:3948px;overflow:hidden;background:var(--white)}
body{position:relative;font-family:'Merriweather',serif;color:var(--text)}
.abs{position:absolute}
.photo{position:absolute}
.btn{position:absolute;display:flex;align-items:center;justify-content:center;background:var(--green);color:var(--white);font-size:15px;width:153px;height:38px;border-radius:2px}
.rule{position:absolute;height:2px;background:var(--tan)}
.sec-title{position:absolute;left:0;width:1200px;text-align:center;color:var(--green);font-size:47px;font-weight:400}
.body-copy{font-size:15.5px;line-height:26px;font-weight:300;color:#333}

/* header */
.hero{left:0;top:0;width:1200px;height:771px;background:linear-gradient(180deg,#fbfbf8 0px,#f3f1ea 120px,#9c8c6d 210px,#7c6a4e 420px,#8f6b4a 600px,#5e4632 771px)}
.brand{left:112px;top:46px;font-size:33px;color:var(--green);font-weight:400;letter-spacing:0.5px}
.contact{display:flex;align-items:center;gap:16px}
.contact .dot{width:48px;height:48px;border-radius:50%;background:var(--green);display:flex;align-items:center;justify-content:center}
.contact .label{color:var(--green);font-size:14px;font-weight:700}
.contact .value{font-size:18px;color:#333;margin-top:6px}
.nav{top:118px;display:flex;gap:0;font-size:15.5px;color:#333}
.nav a{position:absolute;white-space:nowrap;text-decoration:none;color:#333}
.nav a.active{color:var(--tan);border-bottom:1px solid var(--tan);padding-bottom:3px}
.hero-kicker{left:107px;top:232px;font-size:28px;color:var(--white)}
.hero-title{left:107px;top:278px;font-size:55px;color:var(--white);font-weight:400}
.hero-copy{left:107px;top:360px;width:520px;font-size:21px;line-height:30px;color:var(--white)}
.play{left:826px;top:354px;width:62px;height:62px;border-radius:50%;background:var(--green);display:flex;align-items:center;justify-content:center}

/* needs */
.needs-title{left:602px;top:856px;font-size:47px;color:var(--green);font-weight:400}
.needs-copy{left:602px;top:961px;width:490px}

/* regions */
.field-band{left:0;top:1706px;width:1200px;height:410px;background:linear-gradient(180deg,#e9ece2 0%,#7d9b55 25%,#4f7a32 60%,#2f5420 100%)}
.region{position:absolute;top:1729px;width:302px;height:280px;background:var(--white);border-radius:12px;box-shadow:0 0 0 3px rgba(255,255,255,.55);text-align:center}
.region svg{margin-top:56px}
.region .name{font-size:28px;color:var(--green);margin-top:12px}
.region .area{font-size:28px;color:var(--tan);margin-top:6px}

.feature-title{font-size:33px;color:var(--tan);font-weight:400}

/* education */
.edu-band{left:0;top:3064px;width:1200px;height:472px;background:linear-gradient(120deg,#a98b67,#bfa07a 50%,#b69672)}
.edu-quote{left:200px;top:3246px;width:800px;text-align:center;font-size:21px;line-height:30px;color:var(--green)}
.edu-copy{left:200px;top:3322px;width:800px;text-align:center;font-size:15.5px;line-height:26px;color:var(--white);font-weight:300}

/* footer */
.foot-brand{left:112px;top:3690px;font-size:40px;color:var(--green);line-height:52px}
.foot-col h4{font-size:21px;color:var(--green);font-weight:400;margin-bottom:20px}
.foot-col li{list-style:none;font-size:15.5px;color:#333;font-weight:300;margin-bottom:16px}
.copyright{left:0;top:3906px;width:1200px;text-align:center;font-size:14px;color:#333;font-weight:300}
</style>
</head>
<body>

<!-- hero -->
<div class="photo hero" role="img" aria-label="Farmer crouching in a potato field holding harvested potatoes, crates of potatoes and a tractor behind"></div>
<div class="abs brand">Meridale Field Trust</div>

<div class="abs contact" style="left:585px;top:26px">
  <div class="dot"><svg width="22" height="22" viewBox="0 0 24 24"><path fill="#fff" d="M6.6 10.8a15.1 15.1 0 0 0 6.6 6.6l2.2-2.2c.3-.3.7-.4 1-.2 1.1.4 2.3.6 3.6.6.6 0 1 .4 1 1V20c0 .6-.4 1-1 1A17 17 0 0 1 3 4c0-.6.4-1 1-1h3.5c.6 0 1 .4 1 1 0 1.2.2 2.4.6 3.6.1.3 0 .7-.2 1z"/></svg></div>
  <div><div class="label">Call Us</div><div class="value">+ 1 555 014 2270</div></div>
</div>
<div class="abs contact" style="left:885px;top:26px">
  <div class="dot"><svg width="22" height="22" viewBox="0 0 24 24"><path fill="#fff" d="M3 6h18v12H3z"/><path d="M3 6l9 7 9-7" fill="none" stroke="#10683a" stroke-width="2"/></svg></div>
  <div><div class="label">Email</div><div class="value">info@meridale.org</div></div>
</div>

<nav class="abs nav" style="left:0;width:1200px">
  <a class="active" style="left:587px">Home</a>
  <a style="left:712px">About Us</a>
  <a style="left:862px">Solution</a>
  <a style="left:1006px">Contact Us</a>
</nav>

<div class="abs hero-kicker">Welcome To</div>
<h1 class="abs hero-title">Meridale Field Trust</h1>
<p class="abs hero-copy">Namibia is a young democracy in Sub-Saharan Africa with a population of approximately 2.5 Million people.</p>
<div class="abs play"><svg width="22" height="24" viewBox="0 0 22 24"><path d="M3 2l17 10L3 22z" fill="#fff"/></svg></div>

<!-- needs -->
<div class="photo" style="left:112px;top:857px;width:254px;height:237px;background:linear-gradient(160deg,#8aa6c8,#b28a5c 55%,#7a4a35)" role="img" aria-label="Workers harvesting sweet potatoes beside a tractor"></div>
<div class="photo" style="left:112px;top:1131px;width:254px;height:238px;background:linear-gradient(180deg,#6f9ed0,#d7e4ee 35%,#8da650 55%,#b8b468)" role="img" aria-label="Solar panels beside a field of wheat"></div>
<svg class="abs" style="left:170px;top:920px" width="300" height="380" viewBox="0 0 300 380" fill="none" stroke="#10683a" stroke-width="3">
  <path d="M196 8h86v62"/><path d="M282 312v46h-86"/><path d="M4 174v34"/>
</svg>
<div class="photo" style="left:272px;top:990px;width:262px;height:242px;border:3px solid #fff;background:linear-gradient(150deg,#5f8f3a,#2f5a24 60%,#d8d8cf 85%)" role="img" aria-label="Man in a maize field using a tablet"></div>

<h2 class="abs needs-title">Namibia Needs Food</h2>
<div class="rule" style="left:602px;top:915px;width:97px"></div>
<div class="abs needs-copy body-copy">
  <p>Namibia is a young democracy in Sub-Saharan Africa with a population of approximately 2.5 Million people. The country’s agricultural sector has been slow to keep up with the increasing population. As a consequence, approximately 60% of the food required to feed the nation is imported. The elevated cost of these imported foods means a large proportion of the population consume food with low nutritional value.</p>
  <p style="margin-top:33px">Despite vast tracts of available arable land and abundant water resources (both above and below ground), the agricultural sector has struggled to capitalise. This is largely due to a lack of investment, technical knowledge and available technologies.</p>
</div>
<div class="btn" style="left:601px;top:1319px">Read More</div>

<!-- solution -->
<h2 class="sec-title" style="top:1448px">The “Meridale” Solution</h2>
<div class="rule" style="left:551px;top:1522px;width:98px"></div>
<p class="abs" style="left:150px;top:1556px;width:900px;text-align:center;font-size:21.5px;line-height:30px;color:#333">The long term intention of the Meridale Field Trust program would be to establish 3 distinct food production and processing zones which have access to large amounts of arable land, with high quality soil and strong water resources, as well as good transport connections to relevant markets. They are:</p>

<div class="photo field-band" role="img" aria-label="Rows of green crops stretching across a field"></div>
<div class="region" style="left:112px">
  <svg width="78" height="78" viewBox="0 0 78 78" fill="none" stroke="#10683a" stroke-width="3">
    <path d="M60 12A34 34 0 1 0 70 30"/><circle cx="65" cy="20" r="3" fill="#10683a"/>
    <path d="M39 62V22"/><path d="M39 34c-8-2-10-9-9-14 6 0 10 5 9 14zM39 34c8-2 10-9 9-14-6 0-10 5-9 14zM39 48c-9-2-12-9-11-14 7 0 11 6 11 14zM39 48c9-2 12-9 11-14-7 0-11 6-11 14z"/>
  </svg>
  <div class="name">Otavi Region</div>
  <div class="area">Central Namibia</div>
</div>
<div class="region" style="left:449px">
  <svg width="78" height="78" viewBox="0 0 78 78" fill="none" stroke="#10683a" stroke-width="3">
    <circle cx="39" cy="39" r="33"/><path d="M39 18l10 26-10-6-10 6z" fill="#10683a"/>
    <circle cx="39" cy="6" r="3" fill="#10683a"/>
    <text x="34" y="76" font-size="14" fill="#10683a" stroke="none" font-family="Merriweather,serif">N</text>
  </svg>
  <div class="name">Kavango Region</div>
  <div class="area">North Namibia</div>
</div>
<div class="region" style="left:786px">
  <svg width="96" height="88" viewBox="0 0 96 88" fill="none" stroke="#10683a" stroke-width="3">
    <circle cx="48" cy="42" r="28"/><circle cx="48" cy="42" r="18"/><path d="M48 2v24M48 58v12M8 42h24M64 42h24"/>
    <path d="M38 36h20l-10 14z"/>
    <text x="42" y="86" font-size="14" fill="#10683a" stroke="none" font-family="Merriweather,serif">S</text>
  </svg>
  <div class="name" style="margin-top:4px">Neckartal Dam</div>
  <div class="area">South Namibia</div>
</div>

<!-- sustainability -->
<h2 class="sec-title" style="top:2192px">“Meridale” Sustainability</h2>
<div class="rule" style="left:551px;top:2267px;width:98px"></div>

<div class="photo" style="left:112px;top:2331px;width:487px;height:293px;border-radius:3px;background:linear-gradient(180deg,#3f7a2c,#5d9a3a 45%,#7b6040 60%,#c9b38a 80%,#5a4430)" role="img" aria-label="Fresh potatoes in front of rows of potato plants"></div>
<h3 class="abs feature-title" style="left:677px;top:2322px">Processing Facilities</h3>
<p class="abs body-copy" style="left:677px;top:2385px;width:390px">Each of the allocated production zones will be furnished with handling, processing and milling facilities for all crops produced as part of the program. These will include Potatoes, Maize and Wheat.</p>
<div class="btn" style="left:676px;top:2546px">Read More</div>

<h3 class="abs feature-title" style="left:112px;top:2682px">Sustainable Solutions</h3>
<p class="abs body-copy" style="left:112px;top:2745px;width:420px">All irrigation, cropping and production facilities will be operated “off grid” using extensive solar and hydroelectric power generation.In addition, cropping at all sites will be supported with the use of drones for spraying and crop analysis resulting in significant fuel savings and the associated carbon output.</p>
<div class="btn" style="left:112px;top:2931px">Read More</div>
<div class="photo" style="left:599px;top:2682px;width:489px;height:293px;border-radius:3px;background:linear-gradient(180deg,#6d8fb0,#a8b6c2 40%,#8d9494 60%,#4f7a2c 78%,#2f5a1f)" role="img" aria-label="Grain storage silos standing above a maize field"></div>

<!-- education -->
<div class="photo edu-band" role="img" aria-label="Tan-tinted scene of a farmer in a potato field"></div>
<h2 class="sec-title" style="top:3138px;color:var(--white)">“Meridale” Education</h2>
<div class="abs" style="left:551px;top:3205px;width:98px;height:3px;background:var(--green)"></div>
<p class="abs edu-quote">“Give a man a fish and feed him for a day, teach a man to fish and feed him for a lifetime”</p>
<p class="abs edu-copy">Education is key to empowerment and we embrace that concept. As such, we aim to offer a vocational education scheme for the participants in the Meridale Field Trust program. We aim to furnish the participants with the skills to be successful and sustainable farmers in their own rights.</p>
<div class="btn" style="left:523px;top:3416px">Read More</div>

<!-- footer -->
<div class="abs foot-brand">Meridale<br>Field Trust</div>
<div class="abs foot-col" style="left:618px;top:3622px">
  <h4>Quick Links</h4>
  <ul><li>Home</li><li>About Us</li><li>Solution</li><li>Contact Us</li></ul>
</div>
<div class="abs foot-col" style="left:918px;top:3622px">
  <h4>Other Links</h4>
  <ul><li>Terms and conditions</li><li>Privacy policy</li><li>Career</li><li>Help center</li></ul>
</div>
<div class="abs" style="left:112px;top:3916px;width:256px;height:1px;background:var(--tan)"></div>
<div class="abs" style="left:828px;top:3916px;width:260px;height:1px;background:var(--tan)"></div>
<div class="abs copyright">Copyright © 2024 &nbsp;Meridale Field Trust. All rights reserved.</div>

</body>
</html>
```